FACEBOOK PAGE FOR BREVLO PLUMBING GROUP

We need a facebook banner for our new plumbing business.

Needs to be catchy and inline with our logo.

Phone: 0472 836 291
Email: hello@brevlo.com.au
website: www.brevlo.com.au
Servicing: Perth Metro Areas and surrounding suburbs
Services:
*We offer a wide range of services, including:
Plumbing – General maintenance, blocked drains, toilet repairs, burst pipes, reticulation, renovations & emergencies.

*Hot Water – Installation, servicing & repairs for all systems.

*Cooling & Heating – Air conditioning, evaporative cooling & heater servicing.

*Filtration – Filtered taps, under-sink systems & whole-house filtration setups.

Our Mission

Brevlo Group believes plumbing shouldn't break the bank - or your trust. Our mission is to provide honest, affordable, and no-nonsense plumbing services that get the job done right the first time. No runaround - just reliable work, and the respect every customer deserves.

What Makes Us Different???

Upfront Fixed Pricing
No surprises, no hidden fees. You get clear, honest quotes before any work begins.

Respectful, Customer-First Service
We show up on time, communicate clearly, and treat your property like it’s our own.

Locals Serving Locals
We’re proud to support the Perth community with reliable, high-quality plumbing backed by real local care.

FOR THE DESIGNER A little background on us as a new biz for your reference:
By Locals, For Locals
After 13 years in the plumbing industry, seasoned local plumber Wade founded his company to address the widespread issue of homeowners and businesses being overcharged or receiving inferior work. He knew there had to be a better way—and that’s when Brevlo was created.
Today, Brevlo Group is a trusted plumbing company based in Osborne Park, proudly serving residential, commercial, and industrial clients across the Perth metro area. With over a decade of experience, we deliver expert workmanship, fair pricing, and treat every job—big or small—with the same care and professionalism.
Need it done right—and affordably? Get it sorted with BREVLO now!

```html
<!DOCTYPE html>
<html lang="en">
<head>
<meta charset="utf-8">
<title>Brevlo Plumbing Group – Facebook Cover</title>
<link rel="stylesheet" href="https://fonts.googleapis.com/css2?family=Roboto:wght@400;500;700&display=swap">
<style>
  :root {
    --navy: #0d1f6b;
    --navy-deep: #0a1855;
    --sky: #3bb3f0;
    --sky-deep: #1b8de0;
    --accent: #29b6f6;
    --photo-light: #c9d3dc;
    --photo-dark: #5b7ea8;
    --white: #ffffff;
    --ink: #1c2450;
    --page: #ffffff;
  }
  html, body {
    margin: 0;
    width: 1200px;
    height: 1200px;
    overflow: hidden;
    background: var(--page);
    font-family: "Roboto", sans-serif;
  }
  .cover {
    position: absolute;
    left: 50px;
    top: 357px;
    width: 1100px;
    height: 486px;
    background: var(--white);
    overflow: hidden;
  }
  .cover-shapes { position: absolute; inset: 0; }
  .brand {
    position: absolute;
    left: 379px;
    top: 48px;
    transform: translate(-50%, -50%);
    color: var(--white);
    font-weight: 500;
    font-size: 34px;
    letter-spacing: 10px;
  }
  .label {
    position: absolute;
    left: 43px;
    margin: 0;
    color: var(--navy);
    font-weight: 700;
    font-size: 24px;
  }
  .label--servicing { top: 124px; }
  .label--mission { top: 188px; }
  .servicing-area {
    position: absolute;
    left: 43px;
    top: 156px;
    margin: 0;
    color: var(--white);
    font-size: 19px;
  }
  .mission-text {
    position: absolute;
    left: 43px;
    top: 220px;
    width: 440px;
    margin: 0;
    color: var(--white);
    font-size: 15.5px;
    line-height: 19px;
  }
  .services-tab {
    position: absolute;
    left: 43px;
    top: 306px;
    width: 155px;
    height: 37px;
    background: var(--navy);
    border-radius: 10px 10px 0 0;
    color: var(--accent);
    font-weight: 700;
    font-size: 23px;
    line-height: 37px;
    text-align: center;
  }
  .services-list {
    position: absolute;
    left: 43px;
    top: 357px;
    margin: 0;
    padding: 0;
    list-style: none;
    display: grid;
    grid-template-columns: 219px 240px;
    row-gap: 6px;
    color: var(--white);
    font-weight: 500;
    font-size: 21px;
  }
  .services-list .num { color: var(--accent); font-weight: 400; }
  .contact-bar {
    position: absolute;
    left: 43px;
    top: 447px;
    display: flex;
    gap: 52px;
    color: var(--ink);
    font-size: 16px;
  }
  .contact-item { display: flex; align-items: center; gap: 8px; }
  .contact-item svg { width: 15px; height: 15px; fill: var(--ink); }
</style>
</head>
<body>
<section class="cover">
  <svg class="cover-shapes" viewBox="0 0 1100 486" width="1100" height="486">
    <defs>
      <linearGradient id="sky-band" x1="0" y1="0" x2="1" y2="0">
        <stop offset="0" stop-color="var(--sky-deep)"/>
        <stop offset="0.5" stop-color="var(--sky)"/>
        <stop offset="1" stop-color="var(--sky)"/>
      </linearGradient>
      <linearGradient id="photo-tone" x1="0" y1="0" x2="1" y2="1">
        <stop offset="0" stop-color="var(--photo-light)"/>
        <stop offset="1" stop-color="var(--photo-dark)"/>
      </linearGradient>
      <linearGradient id="navy-band" x1="0" y1="0" x2="1" y2="0">
        <stop offset="0" stop-color="var(--navy-deep)"/>
        <stop offset="1" stop-color="var(--navy)"/>
      </linearGradient>
    </defs>
    <path class="top-band" d="M0 0 H1100 V36 H700 L640 96 H0 Z" fill="url(#navy-band)"/>
    <path class="photo-area" role="img" aria-label="Photo of a plumber in a cap and checked shirt fitting a water filter to pipes" d="M720 36 H1100 V468 H780 L690 342 L640 250 L640 150 Z" fill="url(#photo-tone)"/>
    <path class="sky-band" d="M0 96 H760 L690 170 Q660 208 688 250 L760 342 H0 Z" fill="url(#sky-band)" opacity="0.95"/>
    <path class="bottom-band" d="M0 342 H620 L700 432 H0 Z" fill="url(#navy-band)"/>
  </svg>

  <div class="brand">BREVLO</div>

  <h2 class="label label--servicing">Servicing:</h2>
  <p class="servicing-area">Perth Metro Areas and surrounding suburbs</p>

  <h2 class="label label--mission">Our Mission:</h2>
  <p class="mission-text">Brevlo Group delivers trusted, budget friendly plumbing done right, first time. We don’t mess around: reliable service with respect, exactly what you deserve.</p>

  <div class="services-tab">Services:</div>
  <ul class="services-list">
    <li><span class="num">1)</span> Plumbing</li>
    <li><span class="num">2)</span> Filtration</li>
    <li><span class="num">3)</span> Burst Pipes</li>
    <li><span class="num">4)</span> Blocked Drains</li>
  </ul>

  <div class="contact-bar">
    <span class="contact-item">
      <svg viewBox="0 0 16 16" aria-hidden="true"><path d="M8 1a7 7 0 1 0 0 14A7 7 0 0 0 8 1zm0 1.4c.6 0 1.5 1.3 1.9 3.6H6.1C6.5 3.7 7.4 2.4 8 2.4zM2.5 7.3h2.4a13 13 0 0 0 0 1.4H2.5a5.6 5.6 0 0 1 0-1.4zm3.7 0h3.6a11 11 0 0 1 0 1.4H6.2a11 11 0 0 1 0-1.4zm4.9 0h2.4a5.6 5.6 0 0 1 0 1.4h-2.4a13 13 0 0 0 0-1.4zM6.1 10h3.8c-.4 2.3-1.3 3.6-1.9 3.6S6.5 12.3 6.1 10z"/></svg>
      www.brevlo.com.au
    </span>
    <span class="contact-item">
      <svg viewBox="0 0 16 16" aria-hidden="true"><circle cx="8" cy="8" r="7.5"/><path d="M5.6 4.2l1.2 1.6-.7.9c.5 1.1 1.2 1.8 2.3 2.3l.9-.7 1.6 1.2-.7 1.3c-2.7-.3-4.8-2.4-5.1-5.1z" fill="#fff"/></svg>
      0472 836 291
    </span>
    <span class="contact-item">
      <svg viewBox="0 0 16 16" aria-hidden="true"><path d="M1 3.5h14v9H1z"/><path d="M1.5 4l6.5 5 6.5-5" fill="none" stroke="#fff" stroke-width="1.2"/></svg>
      hello@brevlo.com.au
    </span>
  </div>
</section>
</body>
</html>
```